Dore Matin Organics

Need website design for a new company (Trademark: Doré Matin Organics). It's:<br/>-- Organic<br/>-- Raw<br/>-- Plant-based food<br/>-- Kosher<br/> Vegetarian and fruits) concept. Packaging with be completely sustainable. It will essentially be "The Best Food On The Planet." <br/><br/>More info:<br/>a) Main ingredients would be salad, raw zucchini fettuccini noodles, and more plant-based prepared foods; <br/>b) Sauces or dressings to go with the a) above (small portions); <br/>c) Toppings/garnishes; <br/>d) Juices in bottles. <br/><br/>See logos attached. Please design pages for photos of the products which will be packaged for sale (not yet provided). You will notices that there is one logo--the one in color--where the accent is incorrect. We would probably like to use this because it's in color but we need the proper accent above the "e".<br/><br/>We like unusual designs.<br/><br/>Please create in WordPress.<br/><br/>Please send any questions. Thank you for participating.

```html
<!DOCTYPE html>
<html lang="en">
<head>
<meta charset="utf-8">
<title>Doré Matin Organics</title>
<link rel="stylesheet" href="https://fonts.googleapis.com/css2?family=Montserrat:wght@400;500;600;700&family=Playfair+Display:ital,wght@1,400;1,500&family=Oswald:wght@600&display=swap">
<style>
:root{
  --dark:#1f6a3b;
  --deep:#1a5c33;
  --bright:#3daf4a;
  --bright2:#2f9a3e;
  --text:#333;
  --muted:#777;
  --white:#fff;
}
*{margin:0;padding:0;box-sizing:border-box}
html,body{width:1200px;height:4417px;overflow:hidden}
body{font-family:"Montserrat",sans-serif;color:var(--text);background:var(--white);position:relative}
.abs{position:absolute}
.script{font-family:"Playfair Display",serif;font-style:italic;font-weight:400}
.btn{display:inline-block;background:linear-gradient(var(--bright),var(--bright2));color:var(--white);font-family:"Playfair Display",serif;font-style:italic;font-size:18px;text-align:center;line-height:52px;height:52px;width:162px;border-radius:3px}
.lorem{font-size:13px;line-height:27px;color:var(--muted)}
.photo{position:absolute}

/* top bar */
.topbar{top:0;left:0;width:1200px;height:41px;background:var(--dark)}
.social{top:8px;left:77px;display:flex;gap:12px}
.social span{width:26px;height:26px;border-radius:50%;background:var(--bright)}
.phone{top:0;right:77px;height:41px;display:flex;align-items:center;gap:10px;color:var(--white);font-size:15px;font-weight:600}
.phone i{width:24px;height:24px;border-radius:50%;background:var(--bright);display:flex;align-items:center;justify-content:center}

/* nav */
.nav{top:41px;left:0;width:1200px;height:100px;background:var(--white)}
.nav a{position:absolute;top:42px;font-size:15px;color:#222;text-decoration:none}
.nav a.active{color:var(--bright);font-weight:600}
.nav a.active:after{content:"";position:absolute;left:0;right:0;bottom:-12px;height:2px;background:var(--bright)}
.brand{position:absolute;left:543px;top:-26px;width:114px;height:114px;border-radius:50%;background:var(--white);border:2px solid var(--dark);display:flex;align-items:center;justify-content:center;text-align:center;font-size:15px;font-weight:700;color:var(--dark);line-height:18px}

/* hero */
.hero{top:141px;left:0;width:1200px;height:536px;background:radial-gradient(circle at 30% 40%,#d8cdb6,#c9d4b8 40%,#b9ccae 70%,#d9b39c)}
.hero h1{position:absolute;top:212px;width:1200px;text-align:center;font-family:"Oswald",sans-serif;font-weight:600;font-size:56px;letter-spacing:-1px;color:#111}
.hero .tags{position:absolute;left:375px;top:290px;width:451px;height:47px;background:var(--bright);color:var(--white);font-size:22px;font-weight:500;display:flex;align-items:center;justify-content:center;gap:14px}

/* why */
.why{top:677px;left:0;width:1200px;height:422px}
.center{text-align:center;width:1200px;position:absolute}
.why h2{top:56px;font-size:44px;color:var(--dark)}
.why .lorem{top:118px;left:300px;width:600px;text-align:center}
.feature{position:absolute;top:215px;width:200px;text-align:center;font-size:19px;color:#222}
.feature .ring{width:106px;height:106px;margin:0 auto 14px;border:3px solid var(--dark);border-radius:50%;display:flex;align-items:center;justify-content:center}

/* bands */
.band{left:0;width:1200px;background:var(--dark)}
.band .panel{position:absolute;left:729px;width:471px;text-align:center;color:var(--white)}
.band h3{font-size:36px;margin-bottom:14px}
.band p{font-size:13px;line-height:27px;color:#e4efe6;width:320px;margin:0 auto 18px}
.dots{display:flex;justify-content:center;gap:16px;margin-top:30px}
.dots span{width:16px;height:16px;border-radius:50%;border:2px solid var(--white)}
.dots span.on{background:var(--white)}

/* toppings box */
.tbox{top:1651px;left:221px;width:525px;height:291px;border:2px solid var(--dark)}
.tbox h3{position:absolute;left:65px;top:30px;font-size:36px;color:var(--dark)}
.tbox .lorem{position:absolute;left:57px;top:90px;width:310px}
.tbox .btn{position:absolute;left:64px;top:191px}

/* products */
.provide{top:2931px;left:0;width:1200px;height:624px;background:var(--dark)}
.provide h2{top:64px;color:var(--white);font-size:44px}
.provide .lorem{top:130px;left:300px;width:600px;text-align:center;color:#e4efe6}
.card{position:absolute;top:211px;width:245px;height:348px;background:var(--white);text-align:center}
.card .shot{position:absolute;left:42px;top:30px;width:160px;height:190px;border-radius:6px}
.card .name{position:absolute;top:260px;width:100%;font-size:16px;font-weight:700;color:#222}
.card .price{position:absolute;top:290px;width:100%;font-size:16px;color:#333}
.card.hover{background:var(--bright)}
.card.hover .name,.card.hover .price{color:#5bc664}

/* about */
.about{top:3555px;left:0;width:1200px;height:475px}
.about .kicker{position:absolute;left:626px;top:75px;font-size:18px;color:var(--bright)}
.about h2{position:absolute;left:626px;top:105px;font-size:42px;font-weight:400;color:var(--dark)}
.about .lorem{position:absolute;left:626px;width:400px}

/* footer */
.footer{top:4030px;left:0;width:1200px;height:387px;background:var(--dark);color:var(--white);text-align:center}
.footer .fbrand{position:absolute;left:548px;top:42px;width:104px;height:104px;border-radius:50%;border:2px solid var(--white);display:flex;align-items:center;justify-content:center;font-size:15px;font-weight:700;line-height:18px}
.footer .fsocial{position:absolute;top:178px;left:502px;display:flex;gap:10px}
.footer .fsocial span{width:40px;height:40px;border-radius:50%}
.footer .fphone{position:absolute;top:244px;width:1200px;font-size:28px;color:var(--bright);font-weight:500}
.footer .copy{position:absolute;top:303px;width:1200px;font-size:13px}
.footer .links{position:absolute;top:330px;width:1200px;font-size:13px}
</style>
</head>
<body>

<div class="abs topbar">
  <div class="abs social"><span></span><span></span><span></span><span></span></div>
  <div class="abs phone"><i><svg width="13" height="13" viewBox="0 0 24 24"><path fill="#fff" d="M6.6 10.8a15 15 0 0 0 6.6 6.6l2.2-2.2c.3-.3.7-.4 1-.2 1.1.4 2.3.6 3.6.6.6 0 1 .4 1 1V20c0 .6-.4 1-1 1A17 17 0 0 1 3 4c0-.6.4-1 1-1h3.5c.6 0 1 .4 1 1 0 1.3.2 2.5.6 3.6.1.3 0 .7-.2 1z"/></svg></i>555 014 2290</div>
</div>

<nav class="abs nav">
  <a class="active" style="left:287px">Home</a>
  <a style="left:369px">About Us</a>
  <a style="left:459px">Sauces</a>
  <div class="brand">Doré<br>Matin</div>
  <a style="left:703px">Toppings</a>
  <a style="left:797px">Juices</a>
  <a style="left:869px">Contact</a>
  <svg class="abs" style="left:954px;top:45px" width="16" height="16" viewBox="0 0 16 16"><circle cx="6.5" cy="6.5" r="5" fill="none" stroke="#3daf4a" stroke-width="2"/><path d="M10.5 10.5L15 15" stroke="#3daf4a" stroke-width="2"/></svg>
</nav>

<section class="abs hero" role="img" aria-label="Heart-shaped bowls of fruit, nuts, seeds and vegetables on a light wooden table">
  <h1>THE BEST FOOD ON THE PLANET</h1>
  <div class="tags"><span>Sauces</span><span>|</span><span>Toppings</span><span>|</span><span>Juices</span></div>
</section>

<section class="abs why">
  <h2 class="center script">Why Choose Us ?</h2>
  <p class="abs lorem">Lorem Ipsum is simply dummy text of the printing and typesetting industry. Lorem Ipsum has been the industry's standard</p>
  <div class="feature" style="left:120px"><div class="ring"><svg width="56" height="40" viewBox="0 0 56 40" fill="none" stroke="#1f6a3b" stroke-width="2.5"><path d="M4 30c10-2 18 2 24 8M28 38c4-14 14-26 24-32-4 14-10 24-24 32z"/><path d="M6 30c4-8 12-10 18-6-4 6-12 8-18 6z"/></svg></div>Organic</div>
  <div class="feature" style="left:377px"><div class="ring"><svg width="50" height="50" viewBox="0 0 50 50" fill="none" stroke="#1f6a3b" stroke-width="2.5"><circle cx="25" cy="27" r="13"/><path d="M14 14l22 24M25 14l4-6"/></svg></div>Raw</div>
  <div class="feature" style="left:624px"><div class="ring"><svg width="50" height="54" viewBox="0 0 50 54" fill="none" stroke="#1f6a3b" stroke-width="2.5"><path d="M25 16c-6-4-18-2-18 14 0 14 10 20 18 16 8 4 18-2 18-16 0-16-12-18-18-14z"/><path d="M25 16c0-6 2-10 6-12M27 8c6-2 10 0 12 4"/></svg></div>Plant-Based Food</div>
  <div class="feature" style="left:876px"><div class="ring"><svg width="60" height="60" viewBox="0 0 60 60" fill="none" stroke="#1f6a3b" stroke-width="2.5"><path d="M30 6l22 38H8zM30 54L8 16h44z"/></svg></div>Kosher</div>
</section>

<section class="abs band" style="top:1099px;height:447px">
  <div class="photo" style="left:0;top:0;width:729px;height:447px;background:linear-gradient(135deg,#6b6550,#c7a06a 40%,#d77a3a 65%,#7a5a80)" role="img" aria-label="Tongs lifting Thai noodles with shredded carrot and purple cabbage"></div>
  <div class="panel" style="top:97px">
    <h3 class="script">Thai Noodles</h3>
    <p>Lorem Ipsum is simply dummy text of the print and the typesetting industry. Lorem Ipsum has been the industry's standard.</p>
    <span class="btn">SHOP NOW</span>
    <div class="dots"><span class="on"></span><span></span><span></span><span></span></div>
  </div>
</section>

<div class="abs tbox">
  <h3 class="script">Toppings</h3>
  <p class="lorem">Lorem Ipsum is simply dummy text of the print and the typesetting industry. Lorem Ipsum has been the industry's standard.</p>
  <span class="btn">SHOP NOW</span>
</div>
<div class="photo" style="left:606px;top:1590px;width:363px;height:390px;border-radius:45%;background:radial-gradient(circle at 55% 45%,#e24a2c,#e9852e 30%,#4f9a2f 60%,rgba(255,255,255,0) 72%)" role="img" aria-label="Cut-out group of fresh vegetables: lettuce, pepper, carrot, tomato, cucumber, olives and berries"></div>

<section class="abs band" style="top:2016px;height:447px">
  <div class="photo" style="left:0;top:0;width:729px;height:447px;background:linear-gradient(135deg,#3e4a5a,#d9c46a 35%,#b98a5a 55%,#3f7a3a 75%,#b83a3a)" role="img" aria-label="Person in a yellow apron tossing spinach in a wooden salad bowl"></div>
  <div class="panel" style="top:46px">
    <div class="photo" style="position:relative;margin:0 auto 20px;width:76px;height:76px;border-radius:6px;background:linear-gradient(#6da24a,#b8c9a0)" role="img" aria-label="Pouch of dried toppings"></div>
    <h3 class="script">Toppings</h3>
    <p>Lorem Ipsum is simply dummy text of the print and the typesetting industry. Lorem Ipsum has been the industry's standard.</p>
    <span class="btn">SHOP NOW</span>
  </div>
</section>

<section class="abs" style="top:2463px;left:0;width:1200px;height:468px">
  <h3 class="abs script" style="left:234px;top:112px;font-size:36px;line-height:44px;color:var(--dark)">Raw Zucchini Fettuccini<br>Noodles</h3>
  <p class="abs lorem" style="left:237px;top:203px;width:310px">Lorem Ipsum is simply dummy text of the print and the typesetting industry. Lorem Ipsum has been the industry's standard.</p>
  <span class="abs btn" style="left:237px;top:299px">SHOP NOW</span>
  <div class="photo" style="left:704px;top:70px;width:342px;height:340px;border-radius:18px;background:radial-gradient(circle,#9cc35a,#5f8f33 60%,#e4e8e4 80%)" role="img" aria-label="Clear tray of raw zucchini spiral noodles with a product label"></div>
</section>

<section class="abs provide">
  <h2 class="center script">We Provide Our Best</h2>
  <p class="abs lorem">Lorem Ipsum is simply dummy text of the printing and typesetting industry. Lorem Ipsum has been the industry's standard</p>
  <div class="card" style="left:77px"><div class="shot" style="background:radial-gradient(circle,#a8c86a,#e6e8e4 70%)" role="img" aria-label="Tray of zucchini noodles"></div><div class="name">PRODUCT NAME</div><div class="price">$32.00</div></div>
  <div class="card hover" style="left:345px"><div class="shot" style="left:95px;width:55px;background:#4ea94a" role="img" aria-label="Bottle of sauce"></div><svg class="abs" style="left:97px;top:100px" width="50" height="50"><path d="M25 0v50M0 25h50" stroke="#fff" stroke-width="2"/></svg><div class="name">PRODUCT NAME</div><div class="price">$32.00</div></div>
  <div class="card" style="left:609px"><div class="shot" style="left:60px;width:124px;background:linear-gradient(#5aa843,#b7c8a5)" role="img" aria-label="Pouch of toppings"></div><div class="name">PRODUCT NAME</div><div class="price">$32.00</div></div>
  <div class="card" style="left:874px"><div class="shot" style="left:95px;width:55px;background:linear-gradient(#e8ede8 10%,#3d8f2a 18%,#2f7a22)" role="img" aria-label="Bottle of green juice"></div><div class="name">PRODUCT NAME</div><div class="price">$32.00</div></div>
</section>

<section class="abs about">
  <div class="photo" style="left:206px;top:71px;width:342px;height:342px;border-radius:50%;background:linear-gradient(135deg,#cfc7b8,#a08466 45%,#d8d2c8 70%,#7a8a5a)" role="img" aria-label="Woman cooking at a kitchen counter with vegetables and a laptop"></div>
  <div class="kicker">About Us</div>
  <h2>Dore Matin Organics</h2>
  <p class="lorem" style="top:170px">Lorem Ipsum is simply dummy text of the printing and the typesetting industry. Lorem Ipsum has.</p>
  <p class="lorem" style="top:233px">Lorem Ipsum is simply dummy text of the printing and the typesetting industry. Lorem Ipsum has been the industry's standard dummy text ever since the 1500s, when an is on unknown printer took a galley of type and.</p>
  <span class="abs btn" style="left:622px;top:342px">LEARN MORE</span>
</section>

<footer class="abs footer">
  <div class="fbrand">Doré<br>Matin</div>
  <div class="fsocial"><span style="background:#3b5998"></span><span style="background:#2aa3ef"></span><span style="background:#2c70b8"></span><span style="background:#e23a7a"></span></div>
  <div class="fphone">555 014 2290</div>
  <div class="copy">©Dore Matin - 2019 All Rights Reserved.</div>
  <div class="links">Delivery Time &nbsp;|&nbsp; Cost of Delivery &nbsp;|&nbsp; Payment Menthods &nbsp;|&nbsp; Contact Us</div>
</footer>

</body>
</html>
```